Kestonvale Hawks FC Website

We are looking to develop a new website for Kestonvale FC. Kestonvale FC has now joined with Kestonvale Hawks FC and we are looking at a website that can work for both clubs. Kestonvale FC play in a local park football competition while kestonvale Hawks are a Semi Professional team that plays in the Harbourline Premier Division Competition. What we are after is two separate website off the one platform. I have attached both team logos for you to visualise. Also you can look at the existing kestonvale website www.kestonvalefc.com.au. We are looking for a huge improvement in the website and it will be imperative we have links to sponsors and the sponsors can get regular visuals. Weare looking to move this club forward and have a very professional website that can communicate clearly with the community.

Hi All,

Please remember that the website is to represent two clubs;
1. Kestonvale Hawks FC (Competes in Semi Professional League)
2. Kestonvale FC (Compete in TMCJA League which is a lower level)

Further to this the Kestonvale Hawks FC page will require a player profile page which will show photos of each player and a little bio on each.

Thanks

Reason: Would like to spend more time review existing and new designs

```html
<!DOCTYPE html>
<html lang="en">
<head>
<meta charset="utf-8">
<title>Kestonvale FC — Home</title>
<link href="https://fonts.googleapis.com/css2?family=Arimo:wght@400;700&family=Teko:wght@300&display=swap" rel="stylesheet">
<style>
  :root{
    --red:#c8101e;
    --red-deep:#a80a16;
    --red-bright:#d81726;
    --page:#eeeeee;
    --panel:#f8f8f8;
    --white:#ffffff;
    --ink:#333333;
    --ink-soft:#777777;
    --ink-faint:#aaaaaa;
    --line:#d6d6d6;
    --footer:#252525;
    --footer-text:#cfcfcf;
    --social:#2b2b2b;
  }
  *{box-sizing:border-box;margin:0;padding:0}
  html,body{width:1200px;height:1159px;overflow:hidden}
  body{background:var(--page);font-family:"Arimo",Arial,sans-serif;color:var(--ink);position:relative}
  .abs{position:absolute}

  /* header */
  .site-header{position:absolute;left:0;top:0;width:1200px;height:103px;
    background:linear-gradient(180deg,var(--red-deep) 0%,var(--red-bright) 100%)}
  .brand{position:absolute;left:290px;top:34px;display:flex;align-items:center;gap:8px;
    color:var(--white);font-weight:700;font-size:17px;letter-spacing:.3px}
  .brand-dot{width:30px;height:30px;border-radius:50%;background:var(--white)}
  .social{position:absolute;top:41px;width:25px;height:25px;background:var(--social);border-radius:2px}

  /* nav */
  .nav-item{position:absolute;top:119px;height:33px;line-height:33px;font-size:11px;color:#444;
    transform:translateX(-50%);white-space:nowrap}
  .nav-item.is-active{left:290px;width:83px;transform:none;text-align:center;background:var(--red);
    color:var(--white);font-weight:700}

  /* slider */
  .hero{position:absolute;left:290px;top:166px;width:653px;height:274px;
    background:radial-gradient(ellipse at 50% 40%,#6f8a4f 0%,#4d5c3a 45%,#3a3330 100%)}
  .hero-arrow{position:absolute;top:121px;width:31px;height:33px;background:rgba(40,40,40,.75)}
  .hero-arrow svg{display:block;margin:9px auto}
  .hero-dots{position:absolute;left:313px;top:254px;display:flex;gap:3px}
  .hero-dots span{width:9px;height:9px;border-radius:50%;background:#333}
  .hero-dots span.on{background:var(--red)}

  /* info bar */
  .info-bar{position:absolute;left:290px;top:452px;width:653px;height:70px;background:var(--panel)}
  .event-thumb{position:absolute;left:14px;top:12px;width:74px;height:46px;background:linear-gradient(135deg,#2f3a44,#5d87a8)}
  .event-title{position:absolute;left:101px;top:12px;font-size:11px;color:#333}
  .event-date{position:absolute;left:101px;top:29px;font-size:6.5px;font-weight:700;color:#666}
  .more{font-size:6.5px;font-weight:700;color:var(--red)}
  .event-more{position:absolute;left:101px;top:52px}
  .info-divider{position:absolute;left:371px;top:16px;width:1px;height:40px;background:var(--line)}
  .register-label{position:absolute;left:396px;top:21px;font-size:10.5px;font-weight:700;color:var(--red);line-height:16px}
  .register-btn{position:absolute;left:499px;top:20px;width:128px;height:32px;border-radius:4px;
    background:linear-gradient(180deg,var(--red-bright),var(--red-deep));color:var(--white);
    font-size:10.5px;font-weight:700;text-align:center;line-height:32px}

  /* welcome */
  .section-title{position:absolute;top:550px;font-size:14px;font-weight:400;color:#333}
  .section-title em{font-style:normal;color:var(--red)}
  .welcome-lead{position:absolute;left:290px;top:585px;width:220px;font-size:6.5px;font-weight:700;color:#555;line-height:14px}
  .welcome-photo{position:absolute;top:623px;width:92px;height:92px}
  .welcome-body{position:absolute;left:290px;top:731px;width:210px;font-size:6.5px;color:#666;line-height:12.5px}
  .column-divider{position:absolute;left:527px;top:550px;width:1px;height:296px;background:var(--line)}

  /* news */
  .news-card{position:absolute;left:555px;width:388px;height:83px;background:var(--panel)}
  .news-thumb{position:absolute;left:8px;top:9px;width:107px;height:66px;background:linear-gradient(135deg,#e3e0db,#bdb8b0)}
  .news-title{position:absolute;left:124px;top:8px;font-size:10px;font-weight:400;color:#333}
  .news-text{position:absolute;left:124px;top:27px;width:240px;font-size:6.5px;color:#888;line-height:10px}
  .news-dates{position:absolute;left:124px;top:52px;font-size:6.5px;font-weight:700;color:#555}
  .news-more{position:absolute;left:124px;top:67px;font-size:5.5px;color:var(--ink-faint)}

  /* fixtures */
  .fixtures{position:absolute;left:290px;top:892px;width:653px;height:114px;background:var(--panel)}
  .fixtures-badge{position:absolute;left:0;top:0;width:128px;height:114px;background:var(--red);
    color:var(--white);font-family:"Teko",sans-serif;font-weight:300;font-size:29px;line-height:30px;
    text-align:center;padding-top:12px;letter-spacing:.5px}
  .fixtures-badge::after{content:"";position:absolute;right:-8px;top:48px;border-left:8px solid var(--red);
    border-top:8px solid transparent;border-bottom:8px solid transparent}
  .fixture-col{position:absolute;top:21px;list-style:none}
  .fixture-col li{font-size:7px;color:#666;height:13.2px;line-height:13.2px;display:flex;align-items:center;gap:8px}
  .fixture-col li::before{content:"";width:6px;height:6px;background:var(--red)}

  /* footer */
  .site-footer{position:absolute;left:0;top:1048px;width:1200px;height:111px;background:var(--footer)}
  .footer-brand{position:absolute;left:290px;top:28px;width:60px;display:flex;flex-direction:column;
    align-items:center;gap:5px;color:var(--white);font-size:8px;font-weight:700;white-space:nowrap}
  .footer-brand span{width:28px;height:28px;border-radius:50%;background:var(--white)}
  .footer-head{position:absolute;top:28px;font-size:7px;color:var(--white)}
  .footer-links{position:absolute;top:48px;font-size:7px;color:var(--footer-text)}
  .copyright{position:absolute;left:371px;top:73px;font-size:6px;color:#8a8a8a}
  .footer-divider{position:absolute;left:567px;top:18px;width:1px;height:76px;background:#444}
</style>
</head>
<body>

<header class="site-header">
  <div class="brand"><span class="brand-dot"></span>Kestonvale FC</div>
  <span class="social" style="left:823px"></span>
  <span class="social" style="left:855px"></span>
  <span class="social" style="left:887px"></span>
  <span class="social" style="left:919px"></span>
</header>

<nav>
  <a class="nav-item is-active">Home</a>
  <a class="nav-item" style="left:421px">News</a>
  <a class="nav-item" style="left:523px">Fixture &amp; Results</a>
  <a class="nav-item" style="left:635px">Photo Gallery</a>
  <a class="nav-item" style="left:730px">Sponsor</a>
  <a class="nav-item" style="left:804px">Club</a>
  <a class="nav-item" style="left:892px">Contact Us</a>
</nav>

<section class="hero" role="img" aria-label="Photo of young club players in red and white kits listening to their coach on the field">
  <div class="hero-arrow" style="left:1px"><svg width="10" height="16" viewBox="0 0 10 16"><path d="M8 1 2 8l6 7" fill="none" stroke="#bbb" stroke-width="1.5"/></svg></div>
  <div class="hero-arrow" style="right:0"><svg width="10" height="16" viewBox="0 0 10 16"><path d="M2 1l6 7-6 7" fill="none" stroke="#bbb" stroke-width="1.5"/></svg></div>
  <div class="hero-dots"><span class="on"></span><span></span><span></span><span></span><span></span></div>
</section>

<section class="info-bar">
  <div class="event-thumb" role="img" aria-label="News word collage thumbnail"></div>
  <div class="event-title">Charity Day</div>
  <div class="event-date">Sunday 16th march 2014, 11Am Kick Off</div>
  <div class="event-more more">more info</div>
  <div class="info-divider"></div>
  <div class="register-label">Register Online<br>2014 SESSION</div>
  <div class="register-btn">REGISTER ONLINE</div>
</section>

<section class="welcome">
  <h2 class="section-title" style="left:290px">WELCOME to our <em>SITE!</em></h2>
  <p class="welcome-lead">LOREM IPSUM DOLOR SIT AMET, CONSEC TEER ADIPISCING. PRSENT VESTIBULUM.</p>
  <div class="welcome-photo" style="left:291px;background:linear-gradient(180deg,#4a4540,#8a6a48)" role="img" aria-label="Photo of players lined up on a stage at a club presentation"></div>
  <div class="welcome-photo" style="left:403px;background:linear-gradient(180deg,#3a3030,#a2302c)" role="img" aria-label="Photo of an award being handed over at a club event"></div>
  <p class="welcome-body">Lorem ipsum dolor sit amet, conc tetur adipi scing. Praesent vestibuum molstie laculiris. Aenean non ummy drerlauris. Phasellus. porta. Fusce suscipit variusium socila toldnatibus et magis dis parturient montes, nasceidiculus mus. Nulla dui. Fusce feugiatle. suada odio. Morbi nunc odio, gravida at.</p>
  <a class="more abs" style="left:290px;top:814px">more info</a>
</section>

<div class="column-divider"></div>

<section class="news">
  <h2 class="section-title" style="left:555px">Headline <em>NEWS</em></h2>
  <svg class="abs" style="left:936px;top:553px" width="7" height="11" viewBox="0 0 7 11"><path d="M1 1l4.5 4.5L1 10" fill="none" stroke="#c8101e" stroke-width="1.3"/></svg>

  <article class="news-card" style="top:586px">
    <div class="news-thumb" role="img" aria-label="Breaking news newspaper graphic"></div>
    <h3 class="news-title">Information night</h3>
    <p class="news-text">To Parents and players, Kestonvale FC will be holding an information night for Parents on the following nights</p>
    <p class="news-dates">Under 6 – 11 - 5th march at 6:00pm and Under 12 - 16 - 6th March at 6:00pm.</p>
    <a class="news-more">more info</a>
  </article>
  <article class="news-card" style="top:675px">
    <div class="news-thumb" role="img" aria-label="Breaking news newspaper graphic"></div>
    <h3 class="news-title">Information night</h3>
    <p class="news-text">To Parents and players, Kestonvale FC will be holding an information night for Parents on the following nights</p>
    <p class="news-dates">Under 6 – 11 - 5th march at 6:00pm and Under 12 - 16 - 6th March at 6:00pm.</p>
    <a class="news-more">more info</a>
  </article>
  <article class="news-card" style="top:764px">
    <div class="news-thumb" role="img" aria-label="Breaking news newspaper graphic"></div>
    <h3 class="news-title">Information night</h3>
    <p class="news-text">To Parents and players, Kestonvale FC will be holding an information night for Parents on the following nights</p>
    <p class="news-dates">Under 6 – 11 - 5th march at 6:00pm and Under 12 - 16 - 6th March at 6:00pm.</p>
    <a class="news-more">more info</a>
  </article>
</section>

<section class="fixtures">
  <div class="fixtures-badge">FIXTURES<br>&amp;<br>RESULTS</div>
  <ul class="fixture-col" style="left:154px">
    <li>Premier League</li><li>Premier League Res</li><li>Super League</li><li>Super League Res</li><li>Under 16 / 2</li><li>Under 17 / 1</li>
  </ul>
  <ul class="fixture-col" style="left:277px">
    <li>Under 10 / 2</li><li>Under 10 / 3</li><li>Under 11 / 1</li><li>Under 12 / 3</li><li>Under 13 / 3</li><li>Under 14 / 3</li>
  </ul>
  <ul class="fixture-col" style="left:369px">
    <li>AA Men / 5</li><li>AA Men / 6</li><li>AA Men / 8</li><li>AA Men / 10</li><li>AA Men / 10</li><li>AA Men / 14</li>
  </ul>
  <ul class="fixture-col" style="left:455px">
    <li>07 ECL / Red</li><li>07 ECL / Green</li><li>07 ECL / Blue</li><li>08 ECL / Blue</li><li>08 ECL / Green</li><li>09 / Green</li>
  </ul>
  <ul class="fixture-col" style="left:553px">
    <li>06 / A Green</li><li>06 / B Blue</li><li>06 / C Red</li><li>06 / D Purple</li><li>06 / E White</li><li>06 / F Brown</li>
  </ul>
</section>

<footer class="site-footer">
  <div class="footer-brand"><span></span>Kestonvale FC</div>
  <div class="footer-head" style="left:371px">SITE LINK</div>
  <div class="footer-links" style="left:371px">News &nbsp;| &nbsp;Gallery &nbsp;| &nbsp;Sponsor &nbsp;| &nbsp;Contact Us</div>
  <div class="copyright">Kestonvale FC 2014</div>
  <div class="footer-divider"></div>
  <div class="footer-head" style="left:613px">CLUB</div>
  <div class="footer-links" style="left:613px">History &nbsp;| &nbsp;Committee &nbsp;| &nbsp;Awards &nbsp;| &nbsp;Forms</div>
</footer>

</body>
</html>
```